"Vows and Farewells by Meg" Web Site

I would like a web site designed for my funeral and wedding celebrancy business. My logo was designed by Artboard Hive (attached). I have written content of the web pages for reference (attached). I have attached logos designed through artboard hive and photos.
I am sure what else to write in a project description and would welcome suggestions

Target Market(s)

for marriages - brides and grooms, for funerals - families who have lost a loved one

Industry/Entity Type

Wedding Planner

Number of Pages Required

4 page

Font styles to use
Sans Serif

Colors
886aae
3277b5
33a6d7
a64599
e34096

Requirements
Must have
• a call to action (contact me) throughout
Nice to have
• nil
Should not have
• no morbid images

```html
<!DOCTYPE html>
<html lang="en">
<head>
<meta charset="utf-8">
<title>Vows and Farewells by Meg</title>
<link rel="stylesheet" href="https://fonts.googleapis.com/css2?family=Fondamento:ital@0;1&family=Lato:wght@400;700&display=swap">
<style>
:root{
  --purple:#886aae;
  --purple-deep:#3d2380;
  --purple-footer:#8467ad;
  --purple-base:#664a9c;
  --magenta:#a64599;
  --pink:#e34096;
  --cta-band:#c03f98;
  --blue:#3277b5;
  --sky:#33a6d7;
  --ink:#555;
  --white:#fff;
}
*{margin:0;padding:0;box-sizing:border-box}
html,body{width:1200px;height:3169px;overflow:hidden;background:var(--white)}
body{position:relative;font-family:"Lato",sans-serif;color:var(--ink)}
.abs{position:absolute}
.script{font-family:"Fondamento",cursive}

.top-stripe{top:0;left:0;width:1200px;height:5px;
  background:linear-gradient(90deg,var(--purple-deep) 0 12%,var(--pink) 12% 25%,var(--purple-deep) 25% 37%,var(--pink) 37% 50%,var(--purple-deep) 50% 62%,var(--pink) 62% 75%,var(--purple-deep) 75% 87%,var(--pink) 87% 100%)}

.brand{top:30px;left:0;width:1200px;text-align:center}
.brand-dot{width:64px;height:64px;border-radius:50%;background:var(--purple);margin:0 auto 16px;opacity:.85}
.brand-name{font-size:34px;color:var(--purple-deep);letter-spacing:1px;font-weight:400;text-transform:uppercase}

.main-nav{top:200px;left:0;width:1200px;height:30px;font-size:20px;color:var(--pink)}
.main-nav a{position:absolute;color:inherit;text-decoration:none;white-space:nowrap}

.hero{top:262px;left:0;width:1200px;height:571px;
  background:linear-gradient(90deg,#8fa48f 0%,#c6d0c0 22%,#9fb29c 40%,#e9e6e0 55%,#a3b6a0 72%,#c3cebf 88%,#8ea28d 100%)}
.hero-shade{inset:0;background:rgba(40,40,40,.25)}
.hero-title{top:178px;left:0;width:1200px;text-align:center;color:var(--white);font-size:50px;font-style:italic}
.hero-text{top:250px;left:160px;width:880px;text-align:center;color:var(--white);font-size:22px;line-height:36px;font-style:italic}
.hero-dots{top:502px;left:560px;display:flex;gap:6px}
.hero-dots span{width:14px;height:14px;border-radius:50%;border:2px solid var(--white)}
.hero-dots span.on{background:var(--white)}

.section-title{left:0;width:1200px;text-align:center;font-size:46px;font-style:italic}
.lovelife-title{top:890px;color:var(--purple-deep)}

.portrait{border-radius:50%}
.couple-portrait{width:254px;height:254px;top:999px;
  background:radial-gradient(circle,#efe4df 0 48%,#e7b7c3 52%,#c98aa0 70%,#f4eaea 100%)}
.person{width:282px;text-align:center}
.person-name{font-size:25px;color:var(--pink)}
.person-role{font-size:14px;color:var(--purple-deep);letter-spacing:1px;margin-top:6px}
.person-rule{height:2px;background:#bbb;margin:14px 0 22px}
.person-bio{font-size:14px;line-height:25px;color:var(--ink)}

.countdown{top:1021px;left:465px;width:270px;display:grid;grid-template-columns:122px 122px;gap:20px 24px}
.count-box{height:104px;background:var(--purple);border-radius:6px;color:var(--white);text-align:center;padding-top:14px}
.count-num{font-family:"Fondamento",cursive;font-size:42px;line-height:46px}
.count-unit{font-size:20px;font-family:"Fondamento",cursive}

.owner-band{top:1395px;left:0;width:1200px;height:371px;background:linear-gradient(180deg,#9f479f,#c8439a)}
.owner-wave{top:1380px;left:0}
.owner-portrait{top:1283px;left:482px;width:236px;height:236px;border:6px solid var(--pink);
  background:radial-gradient(circle at 50% 40%,#d9b28f 0 30%,#7a5a4a 55%,#3a2e2a 100%)}
.owner-name{top:1544px;left:0;width:1200px;text-align:center;color:var(--white);font-size:27px}
.owner-role{top:1588px;left:0;width:1200px;text-align:center;color:var(--white);font-size:13px;font-style:italic}
.owner-bio{top:1622px;left:200px;width:800px;text-align:center;color:var(--white);font-size:13.5px;line-height:26px}

.cta-band{top:1766px;left:0;width:1200px;height:102px;background:var(--cta-band)}
.cta-text{top:1794px;left:110px;font-size:34px;color:var(--white);font-style:italic;white-space:nowrap}
.cta-button{top:1792px;left:913px;width:177px;height:57px;border-radius:29px;background:var(--white);color:var(--pink);font-size:20px;display:flex;align-items:center;justify-content:center;text-decoration:none}

.ceremonies-title{top:1932px;color:var(--pink)}
.ceremony-list{top:2010px;left:0;width:1200px;text-align:center;font-size:15px;color:#666;word-spacing:2px}

.gallery-photo{width:332px;height:290px}
.more-button{top:2732px;left:501px;width:196px;height:55px;border-radius:28px;background:linear-gradient(90deg,var(--pink),var(--magenta));color:var(--white);font-size:21px;display:flex;align-items:center;justify-content:center;text-decoration:none}

.site-footer{top:2857px;left:0;width:1200px;height:249px;background:var(--purple-footer)}
.footer-base{top:3106px;left:0;width:1200px;height:63px;background:var(--purple-base)}
.footer-heading{top:2918px;font-size:24px;color:var(--white);font-style:italic}
.icon-badge{width:40px;height:40px;border-radius:50%;background:var(--white);display:flex;align-items:center;justify-content:center}
.footer-text{color:var(--white);font-size:15px;line-height:22px}
.footer-brand{top:2935px;left:0;width:1200px;text-align:center}
.footer-brand .brand-dot{background:var(--white);opacity:.9;width:58px;height:58px}
.footer-brand .brand-name{color:var(--white);font-size:30px}
</style>
</head>
<body>
<div class="abs top-stripe"></div>

<header>
  <div class="abs brand">
    <div class="brand-dot"></div>
    <div class="brand-name">Vows and Farewells by Meg</div>
  </div>
  <nav class="abs main-nav script">
    <a style="left:173px">Home</a>
    <a style="left:270px">About Us</a>
    <a style="left:395px">The Wedding</a>
    <a style="left:545px">Funerals</a>
    <a style="left:665px">Other Ceremonies</a>
    <a style="left:843px">Blog</a>
    <a style="left:933px">Contact Us</a>
  </nav>
</header>

<section class="abs hero" role="img" aria-label="Bridesmaids in sage green dresses holding white and red rose bouquets beside the bride">
  <div class="abs hero-shade"></div>
  <h1 class="abs hero-title script">Vows and Farewells by Meg'</h1>
  <p class="abs hero-text script">you are planning a wedding with the love of your life, a funeral to celebrate the life of a loved one or one of many other love and life celebrations, I am glad that you came to 'Vows and Farewells by Meg'</p>
  <div class="abs hero-dots"><span></span><span></span><span class="on"></span><span></span></div>
</section>

<h2 class="abs section-title lovelife-title script">Celebrate our Lovelife</h2>

<div class="abs owner-band"></div>
<svg class="abs owner-wave" width="1200" height="140" viewBox="0 0 1200 140" aria-hidden="true">
  <path d="M0 0 H1200 V40 C1190 90 1140 115 1060 120 C900 130 800 80 700 60 L500 60 C400 80 300 130 140 120 C60 115 10 90 0 40 Z" fill="#fff"/>
</svg>

<div class="abs portrait couple-portrait" style="left:89px" role="img" aria-label="Portrait of the bride framed by a watercolour floral wreath"></div>
<div class="abs portrait couple-portrait" style="left:853px" role="img" aria-label="Portrait of the groom framed by a watercolour floral wreath"></div>

<div class="abs countdown">
  <div class="count-box"><div class="count-num">90</div><div class="count-unit">days</div></div>
  <div class="count-box"><div class="count-num">3</div><div class="count-unit">hours</div></div>
  <div class="count-box"><div class="count-num">11</div><div class="count-unit">mins</div></div>
  <div class="count-box"><div class="count-num">12</div><div class="count-unit">secs</div></div>
</div>

<div class="abs person" style="top:1270px;left:77px">
  <div class="person-name script">Tilly Marsh</div>
  <div class="person-role">BRIDE</div>
  <div class="person-rule"></div>
  <p class="person-bio">Lorem Ipsum is simply dummy text of the printing and typesetting industry. Lorem dummy text ever since the 1500s.</p>
</div>
<div class="abs person" style="top:1270px;left:842px">
  <div class="person-name script">Owen Pryde</div>
  <div class="person-role">GROOM</div>
  <div class="person-rule"></div>
  <p class="person-bio">Lorem Ipsum is simply dummy text of the printing and typesetting industry. Lorem dummy text ever since the 1500s.</p>
</div>

<div class="abs portrait owner-portrait" role="img" aria-label="Portrait of the celebrant, Meg Holloway"></div>
<h3 class="abs owner-name script">Meg Holloway</h3>
<p class="abs owner-role script">owner of Vows and Farewells by Meg</p>
<p class="abs owner-bio">I am also the business owner of Brightpath Leadership Group where I consult to organisations and leaders in the area of leadership development, governance and innovation. I am also a professional non-executive director, sitting on a number of Boards including a port authority. I was previously an academic and have a Doctorate in the area of business administration. My executive career included positions as CEO of Harbourvale and Leadership West.</p>

<div class="abs cta-band"></div>
<p class="abs cta-text script">Falling in love was the easy part,Planning a wedding</p>
<a class="abs cta-button">CONTACT US</a>

<h2 class="abs section-title ceremonies-title script">Our Other Ceremonies</h2>
<p class="abs ceremony-list">Renewal of vows &nbsp;|&nbsp; commitment ceremonies &nbsp;|&nbsp; Baby naming &nbsp; | &nbsp;family commitment ceremonies &nbsp;|&nbsp; MC services at conferences</p>

<div class="abs gallery-photo" style="top:2075px;left:78px;background:linear-gradient(135deg,#e6d6d0,#c48a8a 55%,#7a8ab0)" role="img" aria-label="Friends laughing together at a baby shower"></div>
<div class="abs gallery-photo" style="top:2075px;left:433px;background:linear-gradient(135deg,#d9d4cc,#f1eeea 40%,#3a3c40 75%,#d94c6b)" role="img" aria-label="Bride in a veil embracing the groom with a pink bouquet"></div>
<div class="abs gallery-photo" style="top:2075px;left:790px;background:linear-gradient(135deg,#2a2230,#6b5048 50%,#d6a36a)" role="img" aria-label="Couple sharing a candlelit dinner"></div>
<div class="abs gallery-photo" style="top:2390px;left:78px;background:linear-gradient(90deg,#253a6a 0 45%,#f2efea 55%,#d7d2cb)" role="img" aria-label="Groom in navy suit and bride in lace dress with a red bouquet"></div>
<div class="abs gallery-photo" style="top:2390px;left:433px;background:linear-gradient(135deg,#3a1d1a,#a05a3a 50%,#e0b08a)" role="img" aria-label="Guests raising champagne glasses at a reception"></div>
<div class="abs gallery-photo" style="top:2390px;left:790px;background:linear-gradient(135deg,#ece8e2,#cbbfb4 55%,#8f7f74)" role="img" aria-label="Close-up of hands with wedding rings over white roses"></div>

<a class="abs more-button">MORE PHOTOS</a>

<footer>
  <div class="abs site-footer"></div>
  <div class="abs footer-base"></div>

  <h4 class="abs footer-heading script" style="left:135px">Our Location</h4>
  <div class="abs icon-badge" style="top:2972px;left:77px">
    <svg width="18" height="22" viewBox="0 0 18 22"><path d="M9 0C4 0 0 4 0 9c0 6 9 13 9 13s9-7 9-13c0-5-4-9-9-9z" fill="#e34096"/><circle cx="9" cy="9" r="3.2" fill="#fff"/></svg>
  </div>
  <div class="abs footer-text" style="top:2968px;left:135px;width:230px">
    <div class="script" style="font-style:italic;font-weight:700;font-size:14px">Vows and Farewells by Meg</div>
    <div style="font-size:14px;line-height:19px">Meg Holloway P.O Box 812, Linden 6104, Western Australia</div>
  </div>

  <div class="abs footer-brand">
    <div class="brand-dot"></div>
    <div class="brand-name">Vows and Farewells by Meg</div>
  </div>

  <h4 class="abs footer-heading script" style="left:951px">Contact us</h4>
  <div class="abs icon-badge" style="top:2968px;left:880px">
    <svg width="20" height="20" viewBox="0 0 24 24"><path d="M6.6 10.8a15 15 0 0 0 6.6 6.6l2.2-2.2c.3-.3.7-.4 1-.2 1.1.4 2.3.6 3.6.6.6 0 1 .4 1 1V20c0 .6-.4 1-1 1A17 17 0 0 1 3 4c0-.6.4-1 1-1h3.5c.6 0 1 .4 1 1 0 1.3.2 2.5.6 3.6.1.3 0 .7-.2 1z" fill="#e34096"/></svg>
  </div>
  <div class="abs footer-text" style="top:2977px;left:934px">(+61) 0400 555 019</div>
  <div class="abs icon-badge" style="top:3022px;left:880px">
    <svg width="20" height="16" viewBox="0 0 20 16"><rect width="20" height="16" rx="2" fill="#e34096"/><path d="M1 2l9 7 9-7" stroke="#fff" stroke-width="2" fill="none"/></svg>
  </div>
  <div class="abs footer-text" style="top:3031px;left:934px">meg@vowsfarewells.example</div>
</footer>
</body>
</html>
```